Copper Moth Tattoo

Business card / Appointment card in one

Ive attached the new logo along with a simple format of what I would like written out on the back! Would like a clean/ modern style font to be used! I also attached the current card for a reference of style!

The colors of this would be either white and gold lettering or black with gold lettering.

Email - CopperMothKV@inkmail-demo.com
Ph # 555-482-7319

The message at bottom of back - All cancellations or No Call No Shows within 48 hours of appointment time will result in a forfeit of deposit.

Small block avail (if card is black) to write in appointment date/time

Target Market(s)

Card for Tattoo shop

Contact Information for Business Card

in project description area!

Font styles to use
Sans Serif

Requirements
Must have
• Please refer to current business card photos that were attached as well!
Nice to have
• Looking for blacks, greys and gold for color scheme

```html
<!DOCTYPE html>
<html lang="en">
<head>
<meta charset="utf-8">
<title>Copper Moth Tattoo – Appointment Card</title>
<link rel="stylesheet" href="https://fonts.googleapis.com/css2?family=Cinzel:wght@400;500&display=swap">
<style>
  :root {
    --backdrop: #2a2828;
    --card: #050505;
    --gold: #c9b45a;
    --gold-deep: #9c8a3c;
    --ink-white: #f1efe8;
    --write-in: #f4f3f0;
    --faint: rgba(201, 180, 90, 0.07);
  }
  * { box-sizing: border-box; margin: 0; padding: 0; }
  html, body { width: 1200px; height: 918px; overflow: hidden; }
  body {
    background: var(--backdrop);
    font-family: "Cinzel", "Trajan Pro", serif;
    display: flex;
    align-items: center;
    justify-content: center;
    gap: 80px;
  }
  .card {
    position: relative;
    width: 380px;
    height: 650px;
    background: var(--card);
    overflow: hidden;
  }
  /* Back side: contact and appointment */
  .card-back { text-align: center; }
  .faint-mark {
    position: absolute;
    left: 0; right: 0; top: 200px;
    text-align: center;
    color: var(--faint);
    font-size: 64px;
    line-height: 1.05;
    letter-spacing: 2px;
    pointer-events: none;
  }
  .shop-title {
    position: relative;
    margin-top: 44px;
    color: var(--gold);
    font-size: 38px;
    font-weight: 500;
    letter-spacing: 5px;
    line-height: 1.35;
  }
  .edition {
    position: relative;
    color: #3b3f5a;
    font-size: 11px;
    letter-spacing: 6px;
    margin-top: -2px;
  }
  .contact {
    position: relative;
    margin-top: 44px;
    color: var(--ink-white);
    font-size: 13.5px;
    letter-spacing: 1.6px;
    line-height: 1.9;
  }
  .policy {
    position: relative;
    margin: 56px auto 0;
    width: 310px;
    color: var(--gold);
    font-size: 16px;
    letter-spacing: 2px;
    line-height: 1.55;
    text-transform: uppercase;
  }
  .appointment-slot {
    position: absolute;
    left: 36px; right: 36px; bottom: 36px;
    height: 96px;
    background: var(--write-in);
    border-radius: 18px;
  }
  /* Front side: shop name */
  .card-front {
    display: flex;
    flex-direction: column;
    align-items: center;
    justify-content: center;
    gap: 22px;
  }
  .front-dot {
    width: 14px; height: 14px;
    border-radius: 50%;
    background: var(--gold);
  }
  .front-name {
    color: var(--gold);
    font-size: 46px;
    font-weight: 500;
    letter-spacing: 4px;
    line-height: 1.2;
    text-align: center;
  }
</style>
</head>
<body>
  <section class="card card-back" aria-label="Appointment side">
    <div class="faint-mark" aria-hidden="true">COPPER<br>MOTH<br>TATTOO</div>
    <h1 class="shop-title">Copper Moth<br>Tattoo</h1>
    <p class="edition">VOL 27</p>
    <p class="contact">COPPERMOTHKV@INKMAIL-DEMO.COM<br>555-482-7319</p>
    <p class="policy">All cancellations or no call no shows within 48 hours of appointment time will result in a forfeit of deposit.</p>
    <div class="appointment-slot" aria-label="Space to write appointment date and time"></div>
  </section>

  <section class="card card-front" aria-label="Front side">
    <span class="front-dot"></span>
    <p class="front-name">Copper<br>Moth<br>Tattoo</p>
  </section>
</body>
</html>
```